Template for management consulting firm to use with investors

We need a word template design for delivering content to our clients. Our firm evaluates people and talent within a business and then provides information back to our clients. Many of the deliverables are word based. But there are charts, org charts, occasionally graphs (for example feedback scores or ratings), and tables that collate comparative information. The data needs to be clear and clean. Colors need to work for both evaluative information (red/yellow/green) and non-evaluative (dark blue to light blue). We'd like to make sure that we include our logo and be able to create a clean table of contents. Most of the design/text should be black/blue with colors for different sections/content.

Target Market(s)

Private equity investors and CEOs

Font styles to use
Serif

Colors
0667aa
3389bc
86beda
d1f1f4

Requirements
Must have
• Ability to do either horizontal or vertical format
• Cover page that is easy to print and has space for both client name and corvantine name
• Styles/headings for different levels
• Bullets and quote styles
• Table of contents
• Chart colors
• Header and footer, ideally with way to carry through client name on each page

```html
<!DOCTYPE html>
<html lang="en">
<head>
<meta charset="utf-8">
<title>Project Title Here</title>
<link rel="stylesheet" href="https://fonts.googleapis.com/css2?family=Cinzel:wght@700&family=Cormorant+Garamond:ital,wght@1,500&family=Caladea:wght@700&family=Carlito&display=swap">
<style>
  :root {
    --blue-deep: #0e5d8f;
    --blue-brand: #0667aa;
    --blue-mid: #3389bc;
    --blue-light: #86beda;
    --text: #333333;
    --white: #ffffff;
    --footer-grey: #b0b0b0;
  }
  * { margin: 0; padding: 0; box-sizing: border-box; }
  html, body { width: 1200px; height: 864px; overflow: hidden; background: var(--white); }
  .page { position: relative; width: 1200px; height: 864px; overflow: hidden; background: var(--white); }

  .page-header { position: absolute; left: 0; top: 0; width: 1200px; height: 86px; }
  .project-title {
    position: absolute; left: 16px; top: 28px;
    font-family: "Cinzel", serif; font-weight: 700; font-size: 36px; letter-spacing: 1px;
    color: var(--blue-deep); line-height: 1;
  }
  .client-slot {
    position: absolute; left: 1001px; top: 11px; width: 199px; height: 65px;
    background: var(--blue-deep); color: var(--white);
    font-family: "Carlito", sans-serif; font-size: 23px;
    display: flex; align-items: center; justify-content: center;
  }

  .hero-band {
    position: absolute; left: 0; top: 86px; width: 1200px; height: 240px;
    background: linear-gradient(100deg, #14577f 0%, #1a6593 45%, #145e8c 75%, #1b6a98 100%);
  }
  .hero-statement {
    position: absolute; left: 56px; top: 46px; width: 760px;
    font-family: "Cormorant Garamond", serif; font-style: italic; font-weight: 500;
    font-size: 21px; line-height: 30px; letter-spacing: 0.6px; text-transform: uppercase;
    color: var(--white);
  }

  .content { position: absolute; left: 36px; top: 344px; width: 1140px; }
  .section-heading {
    font-family: "Caladea", serif; font-weight: 700; font-size: 34px; line-height: 1.1;
    color: var(--blue-deep);
  }
  .columns { display: flex; gap: 36px; margin-top: 20px; }
  .column {
    width: 552px; font-family: "Carlito", sans-serif; font-size: 16.5px; line-height: 27px;
    color: var(--text);
  }
  .column p + p { margin-top: 27px; }

  .page-footer { position: absolute; left: 0; top: 826px; width: 1200px; height: 38px; background: var(--footer-grey); }
  .page-number {
    position: absolute; left: 11px; top: 816px; width: 43px; height: 42px;
    background: var(--blue-deep); color: var(--white);
    font-family: "Carlito", sans-serif; font-size: 16px;
    display: flex; align-items: center; justify-content: center;
  }
  .firm-mark {
    position: absolute; left: 1054px; top: 796px; width: 103px; height: 57px;
    background: var(--white);
    display: flex; align-items: center; justify-content: center; gap: 5px;
    font-family: "Caladea", serif; font-weight: 700; font-size: 12px; letter-spacing: 0.5px;
    color: var(--blue-deep);
  }
  .firm-mark .square { width: 7px; height: 7px; background: var(--blue-deep); }
</style>
</head>
<body>
<div class="page">
  <header class="page-header">
    <h1 class="project-title">PROJECT TITLE HERE</h1>
    <div class="client-slot">Client Logo</div>
  </header>

  <section class="hero-band" role="img" aria-label="Blue-toned photograph of a team meeting around a table">
    <p class="hero-statement">Lorem ipsum dolor sit amet, consectetur adipiscing elit, sed do eiusmod tempor incididunt ut labore et dolore magna aliqua. Ut enim ad minim veniam, quis nostrud exercitation ullamco laboris nisi ut aliquip ex ea</p>
  </section>

  <main class="content">
    <h2 class="section-heading">Lorem ipsum dolor sit amet</h2>
    <div class="columns">
      <div class="column">
        <p>Lorem ipsum dolor sit amet, consectetur adipiscing elit, sed do eiusmod tempor incididunt ut labore et dolore magna aliqua. Ut enim ad minim veniam, quis nostrud exercitation ullamco laboris nisi ut aliquip ex ea commodo consequat. Duis aute irure dolor in reprehenderit in voluptate velit esse cillum dolore eu fugiat nulla pariatur. Excepteur sint occaecat cupidatat non proident, sunt in culpa qui officia deserunt mollit anim id est laborum."</p>
        <p>"Sed ut perspiciatis unde omnis iste natus error sit voluptatem accusantium doloremque laudantium, totam rem aperiam, eaque ipsa quae ab illo inventore veritatis et quasi architecto beatae vitae dicta sunt explicabo. Nemo enim ipsam voluptatem quia voluptas sit aspernatur aut odit aut fugit, sed quia consequuntur magni dolores eos qui ratione voluptatem sequi nesciunt. Neque porro quisquam est, qui dolorem</p>
      </div>
      <div class="column">
        <p>Lorem ipsum dolor sit amet, consectetur adipiscing elit, sed do eiusmod tempor incididunt ut labore et dolore magna aliqua. Ut enim ad minim veniam, quis nostrud exercitation ullamco laboris nisi ut aliquip ex ea commodo consequat. Duis aute irure dolor in reprehenderit in voluptate velit esse cillum dolore eu fugiat nulla pariatur. Excepteur sint occaecat cupidatat non proident, sunt in culpa qui officia deserunt mollit anim id est laborum."</p>
        <p>"Sed ut perspiciatis unde omnis iste natus error sit voluptatem accusantium doloremque laudantium, totam rem aperiam, eaque ipsa quae ab illo inventore veritatis et quasi architecto beatae vitae dicta sunt explicabo. Nemo enim ipsam voluptatem quia voluptas sit aspernatur aut odit aut fugit, sed quia consequuntur magni dolores eos qui ratione voluptatem sequi nesciunt. Neque porro quisquam est, qui dolorem</p>
      </div>
    </div>
  </main>

  <footer class="page-footer"></footer>
  <div class="page-number">01</div>
  <div class="firm-mark"><span class="square"></span><span>CORVANTINE</span></div>
</div>
</body>
</html>
```